Re-design of Business Card

We require a design for our business card.

Korrim is a supplier of industrial packaging specializing in plastic products. We are undergoing a rebranding to appear more corporate. We have changed our company name to korrim and have a new logo.

I have uploaded our old card design with the previous company name.
Don't copy the current design. We are looking for a new design.

Industry/Entity Type

Manufacturing

Contact Information for Business Card

please don't copy the current design. we are looking for a new design.

Font styles to use
Sans Serif

Colors

Designer to choose colors to be used in the design.

Requirements
Must have
• clean and easy to read.

```html
<!DOCTYPE html>
<html lang="en">
<head>
<meta charset="utf-8">
<title>Korrim Business Card</title>
<link href="https://fonts.googleapis.com/css2?family=Roboto:wght@400;700;900&display=swap" rel="stylesheet">
<style>
  :root {
    --orange: #f07c1e;
    --charcoal: #2b2b2b;
    --paper: #ffffff;
    --ink: #3a3a3a;
    --rule: #9a9a9a;
    --backdrop: #8f8f8f;
  }
  * { box-sizing: border-box; margin: 0; padding: 0; }
  html, body {
    width: 1200px; height: 900px; overflow: hidden;
    background: var(--backdrop);
    font-family: "Roboto", Arial, sans-serif;
  }
  .card {
    position: absolute;
    width: 560px; height: 320px;
    box-shadow: 0 6px 18px rgba(0,0,0,0.3);
  }
  .card-front { left: 70px; top: 110px; background: var(--charcoal); }
  .card-back { left: 570px; top: 470px; background: var(--paper); }

  .brand-name {
    color: var(--orange);
    font-weight: 900;
    letter-spacing: 2px;
    display: flex; align-items: center; gap: 12px;
  }
  .brand-mark { width: 16px; height: 16px; background: var(--orange); }

  .card-front .brand-name {
    position: absolute; left: 0; right: 0; top: 100px;
    justify-content: center; font-size: 72px;
  }
  .front-footer {
    position: absolute; left: 40px; right: 40px; bottom: 48px;
    display: flex; align-items: center; gap: 14px;
  }
  .front-footer .line { flex: 1; height: 1px; background: var(--orange); }
  .front-url { color: #fff; font-size: 15px; }
  .front-url span { color: var(--orange); }

  .card-back .brand-name {
    position: absolute; left: 34px; top: 128px; font-size: 50px;
  }
  .divider {
    position: absolute; left: 300px; top: 40px; width: 1px; height: 240px;
    background: var(--rule);
  }
  .contact {
    position: absolute; left: 322px; top: 36px; right: 16px;
    color: var(--ink); font-size: 13px; line-height: 1.45;
  }
  .person-name { color: var(--orange); font-weight: 700; font-size: 19px; line-height: 1.1; }
  .person-title { font-size: 13px; margin-bottom: 4px; }
  .section-title { color: var(--orange); font-weight: 700; font-size: 17px; margin: 8px 0 2px; }
  .contact-row { display: flex; align-items: flex-start; gap: 7px; }
  .contact-row svg { flex: none; margin-top: 3px; }
  .indent { padding-left: 19px; }
</style>
</head>
<body>

<section class="card card-front">
  <div class="brand-name"><span class="brand-mark"></span>KORRIM</div>
  <div class="front-footer">
    <span class="line"></span>
    <span class="front-url">www.<span>korrim</span>.com.au</span>
    <span class="line"></span>
  </div>
</section>

<section class="card card-back">
  <div class="brand-name"><span class="brand-mark"></span>KORRIM</div>
  <div class="divider"></div>
  <div class="contact">
    <div class="person-name">DANA WHITLOW</div>
    <div class="person-title">Machinery Sales Manager</div>
    <div class="contact-row">
      <svg width="12" height="12" viewBox="0 0 12 12"><rect width="12" height="12" rx="2" fill="#f07c1e"/><path d="M3.5 3 L5 3 L5.5 4.8 L4.6 5.5 Q5.4 7 6.6 7.5 L7.3 6.6 L9 7.1 L9 8.6 Q5 8.8 3.5 3Z" fill="#fff"/></svg>
      <span>XXXX XXX XXX</span>
    </div>
    <div class="contact-row">
      <svg width="12" height="12" viewBox="0 0 12 12"><rect width="12" height="12" rx="2" fill="#f07c1e"/><rect x="2.5" y="3.5" width="7" height="5" fill="none" stroke="#fff"/><path d="M2.5 3.5 L6 6.4 L9.5 3.5" fill="none" stroke="#fff"/></svg>
      <span>dana@korrim.com.au</span>
    </div>
    <div class="section-title">HEAD OFFICE</div>
    <div class="contact-row">
      <svg width="12" height="12" viewBox="0 0 12 12"><rect width="12" height="12" rx="2" fill="#f07c1e"/><path d="M6 2.3 A2.6 2.6 0 0 1 8.6 4.9 Q8.6 6.6 6 9.7 Q3.4 6.6 3.4 4.9 A2.6 2.6 0 0 1 6 2.3Z" fill="#fff"/><circle cx="6" cy="4.9" r="1" fill="#f07c1e"/></svg>
      <span>48 Harlow St</span>
    </div>
    <div class="indent">Brookfield Vale, Qld</div>
    <div class="indent">4120 Australia</div>
    <div class="contact-row" style="margin-top:6px">
      <svg width="12" height="12" viewBox="0 0 12 12"><rect width="12" height="12" rx="2" fill="#f07c1e"/><path d="M3.5 3 L5 3 L5.5 4.8 L4.6 5.5 Q5.4 7 6.6 7.5 L7.3 6.6 L9 7.1 L9 8.6 Q5 8.8 3.5 3Z" fill="#fff"/></svg>
      <span>1300 555 014</span>
    </div>
    <div class="contact-row">
      <svg width="12" height="12" viewBox="0 0 12 12"><rect width="12" height="12" rx="2" fill="#f07c1e"/><rect x="3" y="5" width="6" height="4" fill="#fff"/><rect x="4" y="2.5" width="4" height="2.5" fill="none" stroke="#fff"/></svg>
      <span>+61 7 5550 1234</span>
    </div>
    <div class="contact-row">
      <svg width="12" height="12" viewBox="0 0 12 12"><rect width="12" height="12" rx="2" fill="#f07c1e"/><circle cx="6" cy="6" r="3.2" fill="none" stroke="#fff"/><path d="M2.8 6 H9.2 M6 2.8 V9.2" stroke="#fff"/></svg>
      <span>www.korrim.com.au</span>
    </div>
  </div>
</section>

</body>
</html>
```